Pelmora Tours - Astronomy in the Kimberley

Pelmora Tours requires a web page to advertise astronomy tours in the East Kimberley, Australia. It needs the following tabs - Home, Tours, Astronomy Events, Gallery, Testimonials, Contacts.

It should target tourists to the Kimberley.
We are unsure of which colours to go with at the moment but we have included our logo if it helps.

It should be mobile and tablet friendly.

Target Market(s)

Families, +40, Tourist, hobby astronomists,

Industry/Entity Type

Events

Number of Pages Required

3 page

Colors
3377b5
ffffff

Requirements
Must have
• Home, Tours, Astronomy Events, Gallery, Calendar, Testimonials, Contacts.
• 'Pelmora Tours' logo
Nice to have
• Pictures of portable amateur telescopes. Pictures of Lake Kununurra or Wyndham.
Should not have
• Pictures of extremely large professional telescopes.

```html
<!DOCTYPE html>
<html lang="en">
<head>
<meta charset="utf-8">
<title>Pelmora Tours – Astronomy in the Kimberley</title>
<link href="https://fonts.googleapis.com/css2?family=Open+Sans:wght@400;700&family=Raleway:wght@300;400;700;800&family=Noto+Serif&display=swap" rel="stylesheet">
<style>
  :root {
    --brand-blue: #3377b5;
    --white: #ffffff;
    --ink: #333333;
    --muted: #a9a9a9;
    --rule: #e2e2e2;
    --footer-bg: #232323;
    --footer-bar: #1d1d1d;
    --footer-text: #cfcfcf;
    --space-deep: #03141c;
    --space-mid: #0d4d5a;
    --space-glow: #2fb0b8;
  }
  * { margin: 0; padding: 0; box-sizing: border-box; }
  html, body { width: 1168px; height: 1200px; overflow: hidden; background: var(--white); }
  body { position: relative; font-family: "Raleway", sans-serif; color: var(--ink); }

  /* Hero */
  .hero {
    position: absolute; left: 0; top: 0; width: 1168px; height: 573px;
    background:
      radial-gradient(ellipse 330px 170px at 560px 330px, #7fb0a8 0%, var(--space-glow) 30%, var(--space-mid) 60%, transparent 85%),
      radial-gradient(ellipse 700px 380px at 600px 360px, #0f5e6c 0%, #082c38 55%, var(--space-deep) 100%);
  }
  .hero-curve { position: absolute; left: 0; top: 549px; width: 1168px; height: 24px; }

  .topbar {
    position: absolute; left: 0; top: 0; width: 1168px; height: 25px;
    border-bottom: 1px solid rgba(255,255,255,.12);
    display: flex; justify-content: center; align-items: center;
    font-size: 10.5px; color: #c9d4d8; font-family: "Raleway", sans-serif;
  }
  .topbar .item { display: flex; align-items: center; gap: 6px; padding: 0 12px; height: 25px; border-right: 1px solid rgba(255,255,255,.12); }
  .topbar .item:last-child { border-right: none; }
  .topbar svg { width: 9px; height: 9px; fill: #c9d4d8; }
  .dot { width: 7px; height: 7px; border-radius: 50%; background: #c9d4d8; display: inline-block; margin-left: 8px; }

  .nav-item { position: absolute; top: 54px; transform: translateX(-50%); text-align: center; color: var(--white); white-space: nowrap; }
  .nav-item .title { font-family: "Open Sans", sans-serif; font-weight: 700; font-size: 11.5px; letter-spacing: .6px; }
  .nav-item .sub { font-family: "Noto Serif", serif; font-size: 10px; letter-spacing: .6px; color: #d5dfe2; margin-top: 3px; }
  .nav-item.active .sub { border-bottom: 1px solid var(--white); padding-bottom: 3px; }

  .brand { position: absolute; left: 584px; top: 52px; transform: translateX(-50%); display: flex; align-items: center; gap: 6px; color: var(--white); font-family: "Raleway", sans-serif; font-weight: 400; font-size: 17px; white-space: nowrap; }
  .brand .mark { width: 10px; height: 10px; border-radius: 50%; background: var(--brand-blue); }

  .hero-kicker { position: absolute; top: 236px; width: 100%; text-align: center; font-family: "Noto Serif", serif; font-size: 13.5px; color: #e6eeee; }
  .hero-rule { position: absolute; top: 267px; left: 551px; width: 66px; height: 1px; background: rgba(255,255,255,.6); }
  .hero-title { position: absolute; top: 288px; width: 100%; text-align: center; font-family: "Raleway", sans-serif; font-weight: 800; font-size: 50px; letter-spacing: -2.5px; color: var(--white); }
  .arrow { position: absolute; top: 282px; width: 20px; height: 18px; }
  .arrow path { fill: none; stroke: rgba(255,255,255,.45); stroke-width: 3; }

  /* Services */
  .section-title { position: absolute; top: 606px; width: 100%; text-align: center; font-weight: 800; font-size: 24.5px; letter-spacing: -1px; color: var(--ink); }
  .section-sub { position: absolute; top: 640px; width: 100%; text-align: center; font-family: "Noto Serif", serif; font-size: 15px; color: var(--muted); letter-spacing: .3px; }
  .section-rule { position: absolute; top: 671px; left: 527px; width: 115px; height: 1px; background: var(--rule); }
  .bookmark { position: absolute; top: 672px; left: 579px; width: 10px; height: 14px; }

  .feature { position: absolute; top: 721px; width: 312px; height: 127px; text-align: center; }
  .feature + .feature { border-left: 1px solid var(--rule); }
  .feature h3 { margin-top: 16px; font-weight: 800; font-size: 14px; letter-spacing: -.6px; color: var(--ink); }
  .feature p { margin-top: 12px; font-weight: 300; font-size: 12px; line-height: 19.5px; color: var(--muted); padding: 0 40px; }

  /* Footer */
  .footer { position: absolute; left: 0; top: 891px; width: 1168px; height: 309px; background: var(--footer-bg); color: var(--footer-text); }
  .footer-edge { position: absolute; left: 0; top: 0; width: 1168px; height: 23px; }
  .footer-brand { position: absolute; left: 154px; top: 84px; display: flex; align-items: center; gap: 7px; font-family: "Raleway", sans-serif; font-size: 21px; color: var(--white); }
  .footer-brand .mark { width: 12px; height: 12px; border-radius: 50%; background: var(--brand-blue); }
  .footer-about { position: absolute; left: 145px; top: 179px; width: 230px; font-size: 12px; line-height: 16.5px; color: var(--footer-text); }
  .footer h4 { position: absolute; top: 64px; font-weight: 400; font-size: 17px; letter-spacing: .5px; color: #dcdcdc; }
  .footer-nav { position: absolute; left: 465px; top: 112px; list-style: none; }
  .footer-nav li { font-size: 12px; line-height: 21px; color: var(--white); display: flex; align-items: center; gap: 8px; }
  .footer-nav svg { width: 5px; height: 8px; }
  .footer-nav path { fill: none; stroke: #bbb; stroke-width: 1.2; }
  .contact-list { position: absolute; left: 788px; top: 112px; list-style: none; }
  .contact-list li { font-size: 12px; line-height: 21px; color: var(--footer-text); display: flex; align-items: center; gap: 10px; }
  .contact-list svg { width: 10px; height: 10px; fill: #ddd; }
  .socials { position: absolute; left: 790px; top: 163px; display: flex; gap: 16px; }
  .socials span { width: 8px; height: 8px; border-radius: 50%; background: #ddd; }
  .contact-btn { position: absolute; left: 786px; top: 187px; width: 122px; height: 26px; border: 1px solid #dcdcdc; display: flex; align-items: center; justify-content: center; gap: 8px; font-size: 10.5px; color: var(--white); }
  .contact-btn svg { width: 11px; height: 9px; }
  .contact-btn rect, .contact-btn path { fill: none; stroke: #fff; stroke-width: 1.1; }
  .footer-bar { position: absolute; left: 0; bottom: 0; width: 1168px; height: 34px; background: var(--footer-bar); text-align: center; line-height: 34px; font-size: 9.5px; color: #bdbdbd; }
  .footer-bar strong { font-weight: 400; color: var(--white); }
</style>
</head>
<body>

<header class="hero" role="img" aria-label="Photograph of a blue spiral galaxy against a starry night sky">
  <div class="topbar">
    <div class="item"><svg viewBox="0 0 10 10"><path d="M2 0l2 2-1 1.5c.8 1.6 1.9 2.7 3.5 3.5L8 6l2 2-1.5 2C4 9.5.5 6 0 1.5z"/></svg>Your Phone Number</div>
    <div class="item"><svg viewBox="0 0 10 10"><path d="M1 6l3-3 1 1-3 3zM5 3l3-3 2 2-3 3-1-1 2-2-.5-.5-2 2z"/></svg>Just a link</div>
    <div class="item">We're social !<span class="dot"></span><span class="dot"></span><span class="dot"></span></div>
  </div>

  <nav>
    <div class="nav-item active" style="left:102px"><div class="title">HOME</div><div class="sub">All starts here</div></div>
    <div class="nav-item" style="left:242px"><div class="title">ASTRONOMY EVENTS</div><div class="sub">About our Events</div></div>
    <div class="nav-item" style="left:386px"><div class="title">TOURS</div><div class="sub">Our Tours Plan</div></div>
    <div class="brand"><span class="mark"></span>Pelmora Tours</div>
    <div class="nav-item" style="left:778px"><div class="title">GALLERY</div><div class="sub">Some Pictures</div></div>
    <div class="nav-item" style="left:907px"><div class="title">TESTIMONIALS</div><div class="sub">Our Clients Opinion</div></div>
    <div class="nav-item" style="left:1044px"><div class="title">CONTACT</div><div class="sub">Let's get in touch</div></div>
  </nav>

  <p class="hero-kicker">Why choose us ?</p>
  <div class="hero-rule"></div>
  <h1 class="hero-title">WE'RE ALWAYS FOR YOU</h1>
  <svg class="arrow" style="left:41px" viewBox="0 0 20 18"><path d="M10 2L3 9l7 7M3 9h16"/></svg>
  <svg class="arrow" style="left:1107px" viewBox="0 0 20 18"><path d="M10 2l7 7-7 7M17 9H1"/></svg>

  <svg class="hero-curve" viewBox="0 0 1168 24" preserveAspectRatio="none"><polygon points="0,1 584,23 1168,1 1168,24 0,24" fill="#ffffff"/></svg>
</header>

<main>
  <h2 class="section-title">WHAT DO WE DO</h2>
  <p class="section-sub">It's all about us</p>
  <div class="section-rule"></div>
  <svg class="bookmark" viewBox="0 0 10 14"><polygon points="0,0 10,0 10,14 5,10 0,14" fill="#e2e2e2"/></svg>

  <section class="feature" style="left:116px"><h3>WHO WE ARE</h3><p>Sample Data Sample Data Sample Data Sample Data Sample Data Sample Data Sample Data Sample Data Sample</p></section>
  <section class="feature" style="left:428px"><h3>WHO WE ARE</h3><p>Sample Data Sample Data Sample Data Sample Data Sample Data Sample Data Sample Data Sample Data Sample</p></section>
  <section class="feature" style="left:740px"><h3>WHO WE ARE</h3><p>Sample Data Sample Data Sample Data Sample Data Sample Data Sample Data Sample Data Sample Data Sample</p></section>
</main>

<footer class="footer">
  <svg class="footer-edge" viewBox="0 0 1168 23" preserveAspectRatio="none"><polygon points="0,0 1168,0 584,22" fill="#ffffff"/></svg>

  <div class="footer-brand"><span class="mark"></span>Pelmora Tours</div>
  <p class="footer-about">Sample Data Sample Data Sample Data Sample Data Sample Data Sample Data Sample Data Sample Data Sample</p>

  <h4 style="left:465px">NAVIGATION</h4>
  <ul class="footer-nav">
    <li><svg viewBox="0 0 5 8"><path d="M1 1l3 3-3 3"/></svg>Home</li>
    <li><svg viewBox="0 0 5 8"><path d="M1 1l3 3-3 3"/></svg>Tours</li>
    <li><svg viewBox="0 0 5 8"><path d="M1 1l3 3-3 3"/></svg>Gallery</li>
    <li><svg viewBox="0 0 5 8"><path d="M1 1l3 3-3 3"/></svg>Testimonials</li>
    <li><svg viewBox="0 0 5 8"><path d="M1 1l3 3-3 3"/></svg>Astronomy Events</li>
  </ul>

  <h4 style="left:786px">CONTACT</h4>
  <ul class="contact-list">
    <li><svg viewBox="0 0 10 10"><path d="M1 0h8v10H1zM3 2v1h1V2zm3 0v1h1V2zM3 5v1h1V5zm3 0v1h1V5z" fill-rule="evenodd"/></svg>Your Address</li>
    <li><svg viewBox="0 0 10 10"><path d="M2 0l2 2-1 1.5c.8 1.6 1.9 2.7 3.5 3.5L8 6l2 2-1.5 2C4 9.5.5 6 0 1.5z"/></svg>Your Phone Number</li>
  </ul>
  <div class="socials"><span></span><span></span><span></span><span></span></div>
  <div class="contact-btn"><svg viewBox="0 0 11 9"><rect x=".5" y=".5" width="10" height="8"/><path d="M.5 .5l5 4 5-4"/></svg>CONTACT FORM</div>

  <div class="footer-bar">© 2015 ALL RIGHTS RESERVED. POWERED BY <strong>PELMORA TOURS</strong>.</div>
</footer>

</body>
</html>
```